Business Card Design for Photographer

Updating business card design. Must use included logo. We're a luxury wedding photography business. Elegancy, luxury, consistency are messages we wish to convey.

Visit our website at www.colbyvarnway.com to familiarize yourself more with our brand design currently (fonts, colors etc.). This is what we want to maintain.

Target Market(s)

Luxury Brides and Grooms

Industry/Entity Type

Wedding

Contact Information for Business Card

Current logo (attached to brief)
Name: Colby Varnway
Phone: 5208813047
website/blog
Email

Requirements
Must have
• Current logo (attached to brief)
• Name: Colby Varnway
• Phone: 5208813047
• website/blog
• Email
• Instagram username
Should not have
• bright colors, fonts that don't suit our brand (visit www.colbyvarnway.com)

```html
<!DOCTYPE html>
<html lang="en">
<head>
<meta charset="utf-8">
<title>Colby Varnway Photographers – Business Cards</title>
<link href="https://fonts.googleapis.com/css2?family=Questrial&family=EB+Garamond:ital@0;1&display=swap" rel="stylesheet">
<style>
  :root {
    --card-dark: #000000;
    --card-light: #efeff1;
    --ink-dark-card: #9a9a9a;
    --ink-light-card: #7a7a7a;
    --mark: #6e6e6e;
    --bg-top: #ffffff;
    --bg-bottom: #c9c9cb;
  }
  * { margin: 0; padding: 0; box-sizing: border-box; }
  html, body { width: 1200px; height: 996px; overflow: hidden; }
  body {
    position: relative;
    background: linear-gradient(160deg, var(--bg-top) 25%, var(--bg-bottom) 100%);
    font-family: "Questrial", "Helvetica Neue", sans-serif;
  }
  .card {
    position: absolute;
    width: 374px;
    height: 214px;
  }
  .card--dark { background: var(--card-dark); color: var(--ink-dark-card); }
  .card--light { background: var(--card-light); color: var(--ink-light-card); }

  /* Front: logo side */
  .brand {
    position: absolute;
    left: 0; right: 0; top: 64px;
    text-align: center;
  }
  .brand__mark {
    display: block;
    width: 34px; height: 34px;
    margin: 0 auto 14px;
    background: var(--mark);
  }
  .brand__name {
    display: block;
    font-size: 17px;
    letter-spacing: 3px;
    text-transform: uppercase;
    line-height: 1;
  }
  .brand__tag {
    display: block;
    margin-top: 8px;
    font-size: 8px;
    letter-spacing: 4px;
    text-transform: uppercase;
    line-height: 1;
  }

  /* Back: contact side */
  .portrait {
    position: absolute;
    left: 17px; top: 44px;
    width: 125px; height: 125px;
    background: linear-gradient(135deg, #4a4a4a 0%, #9b9b9b 45%, #2a2a2a 100%);
  }
  .contact {
    position: absolute;
    left: 159px; top: 42px;
  }
  .contact__name {
    font-size: 15px;
    letter-spacing: 1.2px;
    text-transform: uppercase;
    line-height: 1;
  }
  .contact__role {
    font-family: "EB Garamond", Georgia, serif;
    font-style: italic;
    font-size: 9.5px;
    margin-top: 2px;
    line-height: 1;
  }
  .contact__list {
    list-style: none;
    margin-top: 42px;
    font-size: 11px;
    letter-spacing: 0.5px;
    line-height: 16px;
  }
  .contact__label {
    font-family: "EB Garamond", Georgia, serif;
    font-size: 9px;
    letter-spacing: 0;
  }
</style>
</head>
<body>

  <section class="card card--dark" style="left:44px; top:56px;">
    <div class="brand">
      <span class="brand__mark"></span>
      <span class="brand__name">Colby Varnway</span>
      <span class="brand__tag">Photographers</span>
    </div>
  </section>

  <section class="card card--light" style="left:590px; top:58px;">
    <div class="brand">
      <span class="brand__mark"></span>
      <span class="brand__name">Colby Varnway</span>
      <span class="brand__tag">Photographers</span>
    </div>
  </section>

  <section class="card card--dark" style="left:164px; top:293px;">
    <div class="portrait" role="img" aria-label="Black and white portrait of the photographer"></div>
    <div class="contact">
      <p class="contact__name">Colby Varnway</p>
      <p class="contact__role">photographer</p>
      <ul class="contact__list">
        <li>520.881.3047 <span class="contact__label">(phone)</span></li>
        <li>colby@colbyvarnway.com <span class="contact__label">(e-mail)</span></li>
        <li>colbyvarnwayphoto <span class="contact__label">(instagram)</span></li>
        <li>www.colbyvarnway.com <span class="contact__label">(web/blog)</span></li>
      </ul>
    </div>
  </section>

  <section class="card card--light" style="left:750px; top:293px;">
    <div class="portrait" role="img" aria-label="Black and white portrait of the photographer"></div>
    <div class="contact">
      <p class="contact__name">Colby Varnway</p>
      <p class="contact__role">photographer</p>
      <ul class="contact__list">
        <li>520.881.3047 <span class="contact__label">(phone)</span></li>
        <li>colby@colbyvarnway.com <span class="contact__label">(e-mail)</span></li>
        <li>colbyvarnwayphoto <span class="contact__label">(instagram)</span></li>
        <li>www.colbyvarnway.com <span class="contact__label">(web/blog)</span></li>
      </ul>
    </div>
  </section>

</body>
</html>
```